Selka Varon Photography

I need a website design for my photography business, I want something clean, elegant, Classy.. I like the colors, White, Black, Green/Blue, Pink, Brown, Lavender,, I have a lot added my Logo .... Additional Info... I need a Photography Website Design, with probably 6 Tabs, Home, About Me, Portfolio, Gallery, Investment, Contact.
Home Page should have my logo, Name & Address, Social Media Icons, and Pictures.
As long as the templates are made I have a hosting coming that will code it.
Portraits Photography, Senior Portraits, Newborn, Families, Events, Engagements, Wedding,
Business
5+ page

```html
<!DOCTYPE html>
<html lang="en">
<head>
<meta charset="utf-8">
<title>Selka Varon Photography</title>
<link rel="stylesheet" href="https://fonts.googleapis.com/css2?family=Lato:wght@300;400;700&display=swap">
<style>
  :root {
    --pink: #eba1ca;
    --white: #ffffff;
    --ink: #111111;
    --charcoal: #444444;
    --grey: #b5b5b5;
    --rule: #b9b9b9;
  }
  * { box-sizing: border-box; margin: 0; padding: 0; }
  html, body { width: 1200px; height: 1200px; overflow: hidden; background: var(--white); }
  body { position: relative; font-family: 'Lato', sans-serif; color: var(--ink); }

  .social { position: absolute; left: 31px; top: 146px; display: flex; gap: 2px; }
  .social svg { display: block; }

  .brand { position: absolute; left: 400px; top: 26px; width: 376px; text-align: center; color: var(--charcoal); }
  .brand-mark { display: block; margin: 0 auto; }
  .brand-name { font-weight: 300; font-size: 54px; line-height: 1; margin-top: 8px; letter-spacing: 1px; }
  .brand-sub { font-weight: 300; font-size: 17px; letter-spacing: 9px; margin-top: 8px; }

  .phone { position: absolute; right: 36px; top: 170px; font-size: 26px; color: var(--charcoal); }
  .phone .label { color: var(--grey); font-size: 24px; margin-right: 6px; }

  .rule { position: absolute; left: 35px; width: 1128px; height: 1px; background: var(--rule); }
  .rule.top { top: 222px; }
  .rule.bottom { top: 1028px; }

  .nav { position: absolute; top: 250px; left: 0; font-size: 13px; list-style: none; }
  .nav li { position: absolute; white-space: nowrap; }

  .tile { position: absolute; overflow: hidden; }
  .tile.pink { background: var(--pink); color: var(--white); padding: 21px 18px; }
  .tile h2 { font-weight: 400; font-size: 20px; line-height: 1; }
  .tile p { font-size: 15px; line-height: 20px; margin-top: 12px; }
  .photo .caption { position: absolute; top: 21px; font-weight: 400; font-size: 20px; line-height: 1; }
  .photo .fill { position: absolute; inset: 0; }

  .footer { position: absolute; left: 37px; top: 1047px; font-size: 12px; }
  .footer em { font-weight: 700; }
</style>
</head>
<body>

<div class="social" aria-label="Social media links">
  <svg width="48" height="48" viewBox="0 0 48 48" role="img" aria-label="Social link"><circle cx="24" cy="24" r="22" fill="none" stroke="#111" stroke-width="2.4"/></svg>
  <svg width="48" height="48" viewBox="0 0 48 48" role="img" aria-label="Social link"><circle cx="24" cy="24" r="22" fill="none" stroke="#111" stroke-width="2.4"/></svg>
  <svg width="48" height="48" viewBox="0 0 48 48" role="img" aria-label="Social link"><circle cx="24" cy="24" r="22" fill="none" stroke="#111" stroke-width="2.4"/></svg>
  <svg width="48" height="48" viewBox="0 0 48 48" role="img" aria-label="Social link"><circle cx="24" cy="24" r="22" fill="none" stroke="#111" stroke-width="2.4"/></svg>
</div>

<header class="brand">
  <svg class="brand-mark" width="76" height="76" viewBox="0 0 76 76" aria-hidden="true"><circle cx="38" cy="38" r="38" fill="#444"/></svg>
  <div class="brand-name">selka varon</div>
  <div class="brand-sub">PHOTOGRAPHY</div>
</header>

<div class="phone"><span class="label">TELEPHONE:</span>01632 480 275</div>

<div class="rule top"></div>

<ul class="nav">
  <li style="left:35px">HOME</li>
  <li style="left:119px">ABOUT ME</li>
  <li style="left:246px">PORTFOLIO</li>
  <li style="left:373px">GALLERY</li>
  <li style="left:500px">INVESTMENT</li>
  <li style="left:628px">CONTAC ME</li>
</ul>

<section class="tile pink" style="left:35px; top:293px; width:294px; height:235px;">
  <h2>ABOUT</h2>
  <p>READ ALITTLE MORE ABOUT ME AND MY PHOTOGRAPHY SERVICES</p>
</section>

<section class="tile photo" style="left:331px; top:293px; width:535px; height:235px;">
  <div class="fill" role="img" aria-label="Black and white studio portrait of a small child in a dress" style="background: linear-gradient(90deg, #ffffff 0%, #ffffff 30%, #d8d8d8 55%, #9a9a9a 72%, #e6e6e6 100%);"></div>
  <h2 class="caption" style="left:92px; color:#555;">STUDIO</h2>
</section>

<section class="tile pink" style="left:870px; top:293px; width:294px; height:235px;">
  <h2 style="margin-left:-5px;">OFFERS</h2>
  <p>BE THE FIRST TO FIND OUT ABOUT TH ELATEST SPECIAL OFFERS</p>
</section>

<section class="tile photo" style="left:35px; top:533px; width:567px; height:235px;">
  <div class="fill" role="img" aria-label="Wedding couple embracing outdoors on a sunlit lawn" style="background: linear-gradient(180deg, #b9b39a 0%, #8a8c78 40%, #7f8f5c 70%, #8aa35a 100%);"></div>
  <h2 class="caption" style="left:378px; color:var(--white);">WEDDINGS</h2>
</section>

<section class="tile photo" style="left:607px; top:533px; width:557px; height:235px;">
  <div class="fill" role="img" aria-label="Smiling family of five in blue shirts on a white background" style="background: linear-gradient(180deg, #ffffff 0%, #ffffff 22%, #c9b8ad 50%, #8ea6d2 100%);"></div>
  <h2 class="caption" style="left:168px; color:var(--ink);">FAMILY PORTRAIT</h2>
</section>

<section class="tile pink" style="left:35px; top:772px; width:294px; height:235px;">
  <h2>PRICES</h2>
  <p>CHOOSE SOMETHING THAT SUITS BOTH YOUR STYLE AND YOUR BUDGET</p>
</section>

<section class="tile photo" style="left:331px; top:772px; width:535px; height:235px;">
  <div class="fill" role="img" aria-label="Corporate portrait of a man in a waistcoat against a dark backdrop" style="background: linear-gradient(90deg, #2a2a2a 0%, #3e3e3e 30%, #2c2c2c 60%, #1a1a1a 100%);"></div>
  <h2 class="caption" style="left:351px; color:var(--white);">CORPORATE</h2>
</section>

<section class="tile pink" style="left:870px; top:772px; width:294px; height:235px;">
  <h2 style="margin-left:-1px;">CONTACT ME</h2>
  <p>01632 480 275<br>OR EMAIL<br>INFO@SELKAVARON.COM</p>
</section>

<div class="rule bottom"></div>

<footer class="footer">SELKAVARON <em>&amp;COPYRIGHT</em> 2015</footer>

</body>
</html>
```